Branvique needs a business Card Design

We are looking for a business card Design for our new Managed Service Provider Company, Branvique. Branvique encompasses everything IT for the average medium sized business. Our primary services are help desk support, cyber-security (malware and ransomware protection), and Disaster Recovery systems. We would like the design to have a very clean and professional look, with a very minimalist feel.

Target Market(s)

Medium to large sized businesses

Industry/Entity Type

It Service

Contact Information for Business Card

Name GoesHere
name@branvique.com
O: 555-382-6047
C: 555-731-5820

Font styles to use
Other font styles liked:
• Poppins Font Only Please

Colors

Designer to choose only greyscale colors for use in the design.

Requirements
Must have
• Logo included
Nice to have
• Cutting Edge, innovative, minimalistic, elegant

```html
<!DOCTYPE html>
<html lang="en">
<head>
<meta charset="utf-8">
<title>Branvique Business Card</title>
<link rel="stylesheet" href="https://fonts.googleapis.com/css2?family=Poppins:wght@300;400;600&display=swap">
<style>
  :root {
    --backdrop: #5c5c5c;
    --card: #ffffff;
    --ink: #122a3c;
    --ink-soft: #1f2f3d;
    --mark: #0f3450;
  }
  * { margin: 0; padding: 0; box-sizing: border-box; }
  html, body {
    width: 1200px;
    height: 960px;
    overflow: hidden;
    background: var(--backdrop);
    font-family: "Poppins", sans-serif;
  }
  .stage {
    position: relative;
    width: 1200px;
    height: 960px;
  }
  .card {
    position: absolute;
    left: 260px;
    width: 680px;
    height: 388px;
    background: var(--card);
    border-radius: 28px;
  }
  .card--front { top: 50px; }
  .card--back { top: 512px; }

  .wordmark {
    display: flex;
    align-items: center;
    gap: 14px;
    color: var(--ink);
    font-weight: 400;
    letter-spacing: 0.42em;
    text-transform: uppercase;
  }
  .wordmark__square {
    width: 16px;
    height: 16px;
    background: var(--mark);
    flex: none;
  }
  .wordmark__reg {
    font-size: 10px;
    letter-spacing: 0;
    align-self: flex-start;
    margin-left: -8px;
  }

  .card--front .wordmark {
    position: absolute;
    left: 0;
    right: 0;
    top: 170px;
    justify-content: center;
    font-size: 30px;
  }

  .card--back .wordmark {
    position: absolute;
    left: 62px;
    top: 112px;
    font-size: 28px;
  }

  .contact {
    position: absolute;
    left: 62px;
    bottom: 42px;
    color: var(--ink-soft);
  }
  .contact__name {
    font-size: 22px;
    font-weight: 600;
    color: var(--ink);
    letter-spacing: 0.01em;
    margin-bottom: 8px;
  }
  .contact__list { list-style: none; }
  .contact__item {
    display: flex;
    align-items: center;
    gap: 10px;
    font-size: 16px;
    font-weight: 400;
    line-height: 25px;
  }
  .contact__icon {
    width: 13px;
    height: 13px;
    fill: var(--ink);
    flex: none;
  }
</style>
</head>
<body>
<main class="stage">

  <section class="card card--front" aria-label="Card front">
    <div class="wordmark">
      <span class="wordmark__square"></span>
      <span>Branvique</span><span class="wordmark__reg">®</span>
    </div>
  </section>

  <section class="card card--back" aria-label="Card back">
    <div class="wordmark">
      <span>Branvique</span><span class="wordmark__reg">®</span>
    </div>

    <div class="contact">
      <p class="contact__name">ALEX CARTER</p>
      <ul class="contact__list">
        <li class="contact__item">
          <svg class="contact__icon" viewBox="0 0 16 16" aria-hidden="true"><path d="M3.6 1.2l2.3 2.9-1.3 1.6c.9 2 2.6 3.7 4.6 4.6l1.6-1.3 2.9 2.3-1.5 2.6C6.8 13.6 2.4 9.2 1 3.8z"/></svg>
          <span>555-382-6047</span>
        </li>
        <li class="contact__item">
          <svg class="contact__icon" viewBox="0 0 16 16" aria-hidden="true"><path d="M4 1h8v14H4zM5.4 2.6v9.4h5.2V2.6zM7.2 13h1.6v1H7.2z" fill-rule="evenodd"/></svg>
          <span>555-731-5820</span>
        </li>
        <li class="contact__item">
          <svg class="contact__icon" viewBox="0 0 16 16" aria-hidden="true"><path d="M1 3h14v10H1zM2.2 4.2L8 8.6l5.8-4.4z" fill-rule="evenodd"/></svg>
          <span>alex@branvique.com</span>
        </li>
        <li class="contact__item">
          <svg class="contact__icon" viewBox="0 0 16 16" aria-hidden="true"><circle cx="8" cy="8" r="7"/><path d="M1 8h14M8 1c2.5 2.5 2.5 11.5 0 14M8 1c-2.5 2.5-2.5 11.5 0 14" stroke="#fff" stroke-width="1" fill="none"/></svg>
          <span>www.branvique.com</span>
        </li>
      </ul>
    </div>
  </section>

</main>
</body>
</html>
```